Create a professional, eye-catching business card design that reflects the values and services of Brookfern Veterinary Hospital. we provide veterinary services and the business card should be a memorable representation of the clinic and align with its branding and mission. our tag line is "Gentle Hands for Every Loyal Friend"
Use clean, modern typography. Prioritize readability and professionalism. We would like to see designs that use the color blue, as in the logo example. the final design should communicate professionalism and care, with attention to detail.

```html
<!DOCTYPE html>
<html lang="en">
<head>
<meta charset="utf-8">
<title>Brookfern Veterinary Hospital – Business Card</title>
<link rel="stylesheet" href="https://fonts.googleapis.com/css2?family=Montserrat:wght@500;700;800&family=Cabin:ital,wght@1,600&family=Questrial&display=swap">
<style>
  :root {
    --navy: #1e3163;
    --white: #ffffff;
    --stage: #e9ebf0;
    --grey-curve: #d4d6db;
    --ink-soft: #2a3a66;
  }
  * { margin: 0; padding: 0; box-sizing: border-box; }
  html, body { width: 1200px; height: 947px; overflow: hidden; background: var(--stage); }
  .canvas { position: relative; width: 1200px; height: 947px; }

  .card {
    position: absolute;
    width: 600px; height: 343px;
    border-radius: 18px;
    overflow: hidden;
    box-shadow: 0 14px 30px rgba(20, 30, 60, 0.22);
  }

  /* Front */
  .card-front { left: 60px; top: 80px; background: var(--navy); }
  .front-brand {
    position: absolute; left: 150px; top: 70px;
    display: flex; align-items: center; gap: 22px;
  }
  .brand-circle {
    width: 96px; height: 96px; border-radius: 50%;
    border: 2px solid var(--white);
    flex-shrink: 0;
  }
  .brand-name {
    font-family: "Montserrat", sans-serif; font-weight: 800;
    color: var(--white); line-height: 1; text-transform: uppercase;
  }
  .brand-name .line-main { display: block; font-size: 40px; letter-spacing: 0.5px; }
  .brand-name .line-sub { display: block; font-size: 14.5px; letter-spacing: 1.2px; margin-top: 6px; }
  .front-strip {
    position: absolute; left: 0; bottom: 0; width: 100%; height: 88px;
    background: var(--white);
    display: flex; align-items: center; justify-content: center;
  }
  .tagline {
    font-family: "Cabin", sans-serif; font-style: italic; font-weight: 600;
    font-size: 22px; color: var(--navy); white-space: nowrap;
  }

  /* Back */
  .card-back { left: 540px; top: 500px; background: var(--white); }
  .back-swoosh { position: absolute; inset: 0; }
  .back-brand {
    position: absolute; left: 46px; top: 74px; width: 200px;
    display: flex; flex-direction: column; align-items: center;
  }
  .back-brand .brand-circle { border-color: var(--navy); width: 80px; height: 80px; }
  .back-brand .brand-name { color: var(--navy); text-align: center; margin-top: 14px; }
  .back-brand .line-main { font-size: 30px; }
  .back-brand .line-sub { font-size: 11px; letter-spacing: 0.9px; margin-top: 5px; }
  .divider {
    position: absolute; left: 268px; top: 60px;
    width: 2px; height: 150px; background: var(--navy);
  }
  .contact { position: absolute; left: 292px; top: 58px; color: var(--navy); }
  .person-name { font-family: "Montserrat", sans-serif; font-weight: 700; font-size: 24px; }
  .person-role { font-family: "Questrial", sans-serif; font-size: 15px; color: var(--ink-soft); margin-top: 2px; }
  .contact-list { list-style: none; margin-top: 16px; }
  .contact-list li {
    display: flex; align-items: center; gap: 10px;
    font-family: "Questrial", sans-serif; font-size: 15px; color: var(--ink-soft);
    margin-bottom: 9px; white-space: nowrap;
  }
  .icon-box {
    width: 20px; height: 20px; border: 1.2px solid var(--navy); border-radius: 4px;
    display: flex; align-items: center; justify-content: center; flex-shrink: 0;
  }
</style>
</head>
<body>
<main class="canvas">

  <section class="card card-front" aria-label="Business card front">
    <div class="front-brand">
      <div class="brand-circle"></div>
      <p class="brand-name"><span class="line-main">Brookfern</span><span class="line-sub">Veterinary Hospital</span></p>
    </div>
    <div class="front-strip">
      <p class="tagline">Gentle Hands for Every Loyal Friend</p>
    </div>
  </section>

  <section class="card card-back" aria-label="Business card back">
    <svg class="back-swoosh" width="600" height="343" viewBox="0 0 600 343">
      <path d="M600 150 C 520 190, 430 250, 330 343 L 600 343 Z" fill="var(--navy)"/>
      <path d="M600 190 C 500 220, 410 280, 330 343 L 360 343 C 440 285, 520 230, 600 205 Z" fill="var(--grey-curve)"/>
    </svg>

    <div class="back-brand">
      <div class="brand-circle"></div>
      <p class="brand-name"><span class="line-main">Brookfern</span><span class="line-sub">Veterinary Hospital</span></p>
    </div>

    <div class="divider"></div>

    <div class="contact">
      <p class="person-name">Daniel Whitford</p>
      <p class="person-role">Owner</p>
      <ul class="contact-list">
        <li>
          <span class="icon-box">
            <svg width="12" height="12" viewBox="0 0 24 24" fill="none" stroke="var(--navy)" stroke-width="2"><path d="M5 3h4l2 5-3 2a12 12 0 0 0 6 6l2-3 5 2v4a2 2 0 0 1-2 2A18 18 0 0 1 3 5a2 2 0 0 1 2-2z"/></svg>
          </span>(08) 9364 2218
        </li>
        <li>
          <span class="icon-box">
            <svg width="12" height="12" viewBox="0 0 24 24" fill="none" stroke="var(--navy)" stroke-width="2"><rect x="3" y="5" width="18" height="14" rx="1"/><path d="M3 6l9 7 9-7"/></svg>
          </span>reception@brookfernvet.com.au
        </li>
        <li>
          <span class="icon-box">
            <svg width="12" height="12" viewBox="0 0 24 24" fill="none" stroke="var(--navy)" stroke-width="2"><circle cx="12" cy="12" r="9"/><path d="M3 12h18M12 3c3 3 3 15 0 18M12 3c-3 3-3 15 0 18"/></svg>
          </span>www.brookfernvet.com.au
        </li>
      </ul>
    </div>
  </section>

</main>
</body>
</html>
```